Online medical reviews website needs banner advert!

We need banner advert templates for our website, www.traineepanel.net. These should meet the technical requirements of our partner (uploaded).

Our groundbreaking website allows doctors in training to rate and review their training.

The adverts should use the same modern design language and colour scheme as our website. They should use the text 'Help a junior doctor make a big decision - rate your training!'.

Vector assets should be supplied, allowing us to use alternative text in future.
Updates

Industry/Entity Type

Healthcare

Font styles to use
Other font styles liked:
• Karla

Colors
3277b5
0555a3
ffffff

Requirements
Must have
• Similar design to our website. Should be elegant & modern. Must allow future text to be easily inserted.
Should not have
• Unrelated design.

```html
<!DOCTYPE html>
<html lang="en">
<head>
<meta charset="utf-8">
<title>Trainee Panel – Banner Adverts</title>
<link href="https://fonts.googleapis.com/css2?family=Arimo:wght@400;700&display=swap" rel="stylesheet">
<style>
  :root {
    --page-bg: #e6e6e6;
    --brand-blue: #3277b5;
    --brand-deep: #0555a3;
    --brand-navy: #163a73;
    --brand-sky: #4a8fd0;
    --white: #ffffff;
    --rule-grey: #8c97a3;
    --ink: #111111;
  }
  html, body {
    margin: 0;
    padding: 0;
    overflow: hidden;
  }
  body {
    width: 1200px;
    height: 1200px;
    background: var(--page-bg);
    position: relative;
    font-family: "Arimo", Arial, sans-serif;
  }
  .banner {
    position: absolute;
    left: 60px;
    width: 1080px;
    overflow: hidden;
    background: var(--white);
  }
  .banner--arrow { top: 360px; height: 151px; }
  .banner--button { top: 684px; height: 137px; }
  .banner__bg {
    position: absolute;
    inset: 0;
    width: 100%;
    height: 100%;
  }
  .brand {
    position: absolute;
    left: 24px;
    display: flex;
    align-items: center;
    gap: 10px;
    color: var(--brand-deep);
    font-size: 31px;
    font-weight: 400;
    letter-spacing: -0.5px;
  }
  .banner--arrow .brand { top: 82px; }
  .banner--button .brand { top: 72px; }
  .brand__mark {
    width: 14px;
    height: 14px;
    background: var(--brand-deep);
  }
  .tagline {
    position: absolute;
    margin: 0;
    color: var(--white);
    font-size: 29px;
    font-weight: 400;
    line-height: 34px;
    text-align: right;
  }
  .tagline strong { font-weight: 700; }
  .banner--arrow .tagline { right: 46px; top: 36px; }
  .banner--button .tagline { right: 30px; top: 10px; }
  .cta-arrow {
    position: absolute;
    right: 18px;
    top: 77px;
    width: 14px;
    height: 20px;
  }
  .cta-button {
    position: absolute;
    left: 893px;
    top: 96px;
    width: 140px;
    height: 29px;
    box-sizing: border-box;
    background: var(--white);
    border: 2px solid var(--brand-navy);
    border-radius: 2px;
    color: var(--ink);
    font-size: 21px;
    line-height: 25px;
    text-align: center;
  }
</style>
</head>
<body>

  <section class="banner banner--arrow">
    <svg class="banner__bg" viewBox="0 0 1080 151" preserveAspectRatio="none">
      <defs>
        <linearGradient id="blueSweep" x1="0" y1="0" x2="1" y2="0">
          <stop offset="0" stop-color="#5b9bd8"/>
          <stop offset="0.6" stop-color="var(--brand-blue)"/>
          <stop offset="1" stop-color="var(--brand-deep)"/>
        </linearGradient>
      </defs>
      <polygon points="0,0 1080,0 1080,151 1010,151 0,18" fill="url(#blueSweep)"/>
      <polygon points="0,18 1010,151 960,151 0,34" fill="#cfe0f1" opacity="0.6"/>
      <line x1="0" y1="38" x2="640" y2="122" stroke="var(--rule-grey)" stroke-width="2"/>
    </svg>
    <div class="brand"><span class="brand__name">Trainee Panel</span><span class="brand__mark"></span></div>
    <p class="tagline">Help a junior doctor make a <strong>BIG DECISION</strong><br>- rate your training!</p>
    <svg class="cta-arrow" viewBox="0 0 14 20"><polygon points="0,0 14,10 0,20" fill="var(--brand-navy)"/></svg>
  </section>

  <section class="banner banner--button">
    <svg class="banner__bg" viewBox="0 0 1080 137" preserveAspectRatio="none">
      <defs>
        <linearGradient id="deepSweep" x1="0" y1="0" x2="1" y2="1">
          <stop offset="0" stop-color="#2a6cae"/>
          <stop offset="0.5" stop-color="var(--brand-blue)"/>
          <stop offset="1" stop-color="var(--brand-deep)"/>
        </linearGradient>
      </defs>
      <polygon points="0,0 1080,0 1080,137 756,137 0,36" fill="url(#deepSweep)"/>
      <polygon points="0,36 756,137 700,137 0,50" fill="#d7e5f3" opacity="0.55"/>
      <polygon points="740,137 1080,62 1080,137" fill="var(--brand-navy)"/>
    </svg>
    <div class="brand"><span class="brand__name">Trainee Panel</span><span class="brand__mark"></span></div>
    <p class="tagline">Help a junior doctor make a <strong>BIG DECISION</strong><br>- rate your training!</p>
    <div class="cta-button">Click Here</div>
  </section>

</body>
</html>
```